Letterhead design for Sleep Consulting Business

I'm looking for a new letterhead (heading/footer) design for my Sleep Consulting Business, I work with families to help their children improve their sleep.

The heading/footer will used in Microsoft Word Only-to be used for all of my documents such as writing Sleep Plans. I need to utilize as much working space in the document as possible. This will NOT be printed out on paper- it will only be used for heading/footer on microsoft word, then emailed to clients, who may print it at home.

My brand colors:
Dark Blue Hex: 1F2A42
Lighter Blueish Hex: 90BEC9
You're welcome to check out my website for inspiration- it is freshly created with other colors as well, and I love the outcome. www.hollowpinerest.com

Target Market(s)

Tired parents

Font styles to use
Script
Other font styles liked:
• Great Vibe, Lato or Just Another Hand are all used currently for my brand. Open to other options.

Requirements
Must have
• The letterhead (heading/footer) MUST be kept narrow (height-wise), so I have plenty of space on my document, while including important information.

It should look professional on screen, and when printed.

Must include my business name OR logo (Hollow Pine Sleep Consulting), and my email address. Mara@hollowpinerest.com

Website is optional, not required, just if you need to fill in a spot: www.hollowpinerest.com

```html
<!DOCTYPE html>
<html lang="en">
<head>
<meta charset="utf-8">
<title>Hollow Pine Sleep Consulting – Letterhead</title>
<link href="https://fonts.googleapis.com/css2?family=Montserrat:wght@600;700&display=swap" rel="stylesheet">
<style>
  :root {
    --navy: #1F2A42;
    --mist: #90BEC9;
    --paper: #FFFFFF;
    --backdrop: #FFFFFF;
  }
  html, body {
    margin: 0;
    padding: 0;
    width: 1200px;
    height: 1200px;
    overflow: hidden;
    background: var(--backdrop);
  }
  .canvas {
    position: relative;
    width: 1200px;
    height: 1200px;
  }
  .letterhead {
    position: absolute;
    left: 285px;
    top: 154px;
    width: 631px;
    height: 892px;
    display: block;
    background: var(--paper);
  }
  .navy-fill { fill: var(--navy); }
  .mist-fill { fill: var(--mist); }
  .paper-line { fill: none; stroke: var(--paper); stroke-width: 4; }
  .brand-name {
    font-family: "Montserrat", sans-serif;
    font-weight: 600;
    font-size: 17px;
    fill: var(--paper);
  }
  .brand-mark { fill: var(--paper); }
  .contact-text {
    font-family: "Montserrat", sans-serif;
    font-weight: 700;
    font-size: 14.5px;
    fill: var(--navy);
  }
  .contact-icon { fill: var(--navy); }
  .contact-icon-line { fill: none; stroke: var(--paper); stroke-width: 1.4; }
</style>
</head>
<body>
<div class="canvas">
  <svg class="letterhead" viewBox="0 0 673 952" xmlns="http://www.w3.org/2000/svg" aria-label="Hollow Pine Sleep Consulting letterhead">
    <!-- header band -->
    <g class="header">
      <path class="navy-fill" d="M0,0 H673 V142 C570,82 450,78 312,124 C250,150 200,172 140,172 C80,172 30,150 0,130 Z"/>
      <path class="paper-line" d="M312,124 C420,55 560,22 673,62"/>
      <path class="mist-fill" d="M312,124 C420,55 560,22 673,62 V86 C560,56 430,70 312,124 Z"/>
      <path class="paper-line" d="M312,124 C430,70 560,56 673,86"/>
      <circle class="brand-mark" cx="82" cy="79" r="18"/>
      <text class="brand-name" x="112" y="85">Hollow Pine Sleep Consulting</text>
    </g>

    <!-- footer band -->
    <g class="footer">
      <path class="navy-fill" d="M365,952 C430,905 520,870 673,815 V952 Z"/>
      <path class="mist-fill" d="M405,952 C480,900 560,850 650,822 L673,815 L673,820 C590,850 520,900 470,952 Z"/>
      <path class="paper-line" d="M405,952 C480,900 560,850 650,822"/>
      <path class="paper-line" d="M470,952 C520,900 590,850 673,820"/>
    </g>

    <!-- contact details -->
    <g class="contacts">
      <g class="contact-row phone">
        <path class="contact-icon" d="M55,811 l5,-3 4,6 -3,3 c1,3 4,6 7,7 l3,-3 6,4 -3,5 c-9,1 -20,-10 -19,-19 z"/>
        <text class="contact-text" x="84" y="826">555-201-3380</text>
      </g>
      <g class="contact-row email">
        <rect class="contact-icon" x="52" y="846" width="21" height="15" rx="1"/>
        <path class="contact-icon-line" d="M53,847 L62.5,855 L72,847"/>
        <text class="contact-text" x="84" y="860">Mara@hollowpinerest.com</text>
      </g>
      <g class="contact-row web">
        <circle class="contact-icon" cx="63" cy="891" r="11"/>
        <ellipse class="contact-icon-line" cx="63" cy="891" rx="4.5" ry="11"/>
        <path class="contact-icon-line" d="M52,891 H74 M54,885 H72 M54,897 H72 M63,880 V902"/>
        <text class="contact-text" x="84" y="896">www.hollowpinerest.com</text>
      </g>
    </g>
  </svg>
</div>
</body>
</html>
```